Business Cards

I'd like help creating business cards with the full logo "Veltrona Capital Partners" on the back of the card (navy background with white writing), and abbreviated logo "VCP" on the front. Would like to list name, title, phone number, email, and website listed on front of card. Would like to keep very simple. Front font Arial or similar.

```html
<!DOCTYPE html>
<html lang="en">
<head>
<meta charset="utf-8">
<title>Veltrona Capital Partners – Business Cards</title>
<link href="https://fonts.googleapis.com/css2?family=Arimo:wght@400;700&family=Montserrat:wght@600&display=swap" rel="stylesheet">
<style>
  :root {
    --navy: #1f3869;
    --ink: #23214f;
    --paper: #ffffff;
    --backdrop: #eeeeee;
    --rule: #e3e3e3;
  }
  * { margin: 0; padding: 0; box-sizing: border-box; }
  html, body { width: 1200px; height: 979px; overflow: hidden; }
  body { background: var(--backdrop); position: relative; font-family: "Arimo", Arial, sans-serif; }

  .card {
    position: absolute;
    left: 375px;
    width: 528px;
    height: 301px;
    box-shadow: 10px 10px 10px rgba(0,0,0,0.45);
  }
  .card--back { top: 157px; background: var(--navy); }
  .card--front { top: 536px; background: var(--paper); }

  .wordmark {
    position: absolute;
    left: 0; right: 0;
    top: 112px;
    text-align: center;
    color: var(--paper);
    font-family: "Montserrat", Arial, sans-serif;
    font-weight: 600;
    line-height: 1.25;
  }
  .wordmark__name { display: block; font-size: 42px; letter-spacing: 3px; }
  .wordmark__sub { display: block; font-size: 17px; letter-spacing: 6px; }

  .monogram {
    position: absolute;
    left: 46px;
    top: 118px;
    width: 160px;
    text-align: center;
    color: var(--navy);
    font-weight: 700;
    font-size: 54px;
    letter-spacing: 1px;
  }

  .divider {
    position: absolute;
    left: 246px;
    top: 50px;
    width: 1px;
    height: 194px;
    background: var(--rule);
  }

  .person {
    position: absolute;
    left: 283px;
    top: 62px;
    color: var(--navy);
  }
  .person__name { font-size: 27px; font-weight: 400; letter-spacing: 0.3px; }
  .person__name strong { font-weight: 700; }
  .person__title { font-size: 18px; margin-top: 4px; margin-left: 4px; }

  .contacts {
    position: absolute;
    left: 283px;
    top: 148px;
    list-style: none;
  }
  .contacts li {
    display: flex;
    align-items: center;
    height: 27px;
    margin-bottom: 9px;
    color: var(--ink);
    font-size: 14.5px;
  }
  .contacts li:nth-child(3) { margin-top: -3px; }
  .contacts svg { width: 27px; height: 27px; margin-right: 13px; flex: none; }
</style>
</head>
<body>

<section class="card card--back" aria-label="Card back">
  <div class="wordmark">
    <span class="wordmark__name">VELTRONA</span>
    <span class="wordmark__sub">CAPITAL PARTNERS</span>
  </div>
</section>

<section class="card card--front" aria-label="Card front">
  <div class="monogram">VCP</div>
  <div class="divider"></div>

  <div class="person">
    <h1 class="person__name"><strong>MARINA</strong> HOLT</h1>
    <p class="person__title">IT DIRECTOR</p>
  </div>

  <ul class="contacts">
    <li>
      <svg viewBox="0 0 28 28" aria-hidden="true">
        <circle cx="14" cy="14" r="14" fill="#1f3869"/>
        <path d="M10 8.5l2 0 1 3-1.5 1.2a8 8 0 0 0 3.8 3.8L16.5 15l3 1v2a1.5 1.5 0 0 1-1.6 1.5A10 10 0 0 1 8.5 10.1 1.5 1.5 0 0 1 10 8.5z" fill="#fff"/>
      </svg>
      555-204-7731
    </li>
    <li>
      <svg viewBox="0 0 28 28" aria-hidden="true">
        <circle cx="14" cy="14" r="14" fill="#1f3869"/>
        <rect x="8" y="10" width="12" height="8.5" fill="none" stroke="#fff" stroke-width="1.3"/>
        <path d="M8 10l6 5 6-5M8 18.5l4.5-4M20 18.5l-4.5-4" fill="none" stroke="#fff" stroke-width="1.1"/>
      </svg>
      marinaholt@vcp.com
    </li>
    <li>
      <svg viewBox="0 0 28 28" aria-hidden="true">
        <circle cx="14" cy="14" r="14" fill="#1f3869"/>
        <g fill="none" stroke="#fff" stroke-width="1.2">
          <circle cx="14" cy="14" r="6.5"/>
          <ellipse cx="14" cy="14" rx="3" ry="6.5"/>
          <path d="M7.5 14h13M8.5 10.5h11M8.5 17.5h11"/>
        </g>
      </svg>
      www.vcp.com
    </li>
  </ul>
</section>

</body>
</html>
```